Accounting and Financial Services Firm - Modern, Fresh, Original, Professional

We need a business card designed. We would like to see use of the the colors blue. Logo attached.

Modern, Fresh, Original, Professional,
Updates

Email section on business card required. design brief updated.

Target Market(s)

Small to medium businesses and high net worth individuals

Industry/Entity Type

Public Accounting

Contact Information for Business Card

Business Name: PL Ledgerworth Chartered Accountants
Address: Level 9, 42 Garnet Lane Sydney NSW 2000
Ph: 02 9314 2758
Mobile: 04 XXXX XXXX
Email: mara@plledgerworth.com.au
Wechat ID: XXXXXXX
Website: www.plledgerworth.com.au

Name: Mara Osei
Position: Manager

Font styles to use
Sans Serif

Colors
0492cd
33a6d7
85cae6

Requirements
Must have
• Modern font.

```html
<!DOCTYPE html>
<html lang="en">
<head>
<meta charset="utf-8">
<title>PL Ledgerworth Chartered Accountants – Business Card</title>
<link rel="stylesheet" href="https://fonts.googleapis.com/css2?family=Roboto:wght@400;500&family=Roboto+Condensed:wght@700&display=swap">
<style>
  :root {
    --backdrop: #2b2b2c;
    --card: #1f1f20;
    --blue: #0492cd;
    --blue-mid: #33a6d7;
    --blue-light: #85cae6;
    --text-light: #f2f2f2;
    --text-grey: #9a9a9a;
    --divider: #6d6d6d;
  }
  * { margin: 0; padding: 0; box-sizing: border-box; }
  html, body {
    width: 1200px;
    height: 900px;
    overflow: hidden;
    background: var(--backdrop);
  }
  .canvas {
    position: relative;
    width: 1200px;
    height: 900px;
  }
  .card {
    position: absolute;
    left: 300px;
    width: 600px;
    height: 364px;
    background: var(--card);
    box-shadow: 0 6px 18px rgba(0,0,0,0.35);
    font-family: "Roboto", Arial, sans-serif;
    color: var(--text-light);
  }
  .card--front { top: 68px; }
  .card--back { top: 468px; }

  /* Front */
  .brand {
    position: absolute;
    top: 104px;
    left: 0;
    width: 100%;
    display: flex;
    justify-content: center;
    align-items: center;
    gap: 14px;
  }
  .brand__square {
    width: 30px;
    height: 30px;
    background: var(--blue);
  }
  .brand__name {
    font-weight: 500;
    color: var(--blue);
    line-height: 1.05;
    text-transform: uppercase;
  }
  .brand__title {
    display: block;
    font-size: 36px;
    letter-spacing: 1px;
  }
  .brand__tagline {
    display: block;
    font-size: 12px;
    letter-spacing: 3.2px;
    margin-top: 4px;
  }
  .front-website {
    position: absolute;
    top: 252px;
    left: 0;
    width: 100%;
    text-align: center;
    font-size: 15px;
    letter-spacing: 5px;
    color: var(--text-light);
  }

  /* Back */
  .person {
    position: absolute;
    top: 112px;
    right: 346px;
    text-align: right;
  }
  .person__name {
    font-family: "Roboto Condensed", "Arial Narrow", sans-serif;
    font-weight: 700;
    font-size: 34px;
    line-height: 1;
    color: var(--blue);
    text-transform: uppercase;
  }
  .person__role {
    font-family: "Roboto Condensed", "Arial Narrow", sans-serif;
    font-weight: 700;
    font-size: 17px;
    color: var(--text-grey);
    letter-spacing: 0.5px;
    text-transform: uppercase;
    margin-top: 4px;
  }
  .divider {
    position: absolute;
    top: 90px;
    left: 272px;
    width: 1px;
    height: 108px;
    background: var(--divider);
  }
  .contacts {
    position: absolute;
    top: 94px;
    left: 292px;
    list-style: none;
  }
  .contacts__item {
    display: flex;
    align-items: center;
    gap: 10px;
    font-size: 16px;
    font-weight: 500;
    line-height: 20px;
    color: var(--text-light);
  }
  .icon {
    width: 14px;
    height: 14px;
    flex: none;
    fill: var(--blue-mid);
  }
  .address {
    position: absolute;
    top: 268px;
    left: 86px;
    display: flex;
    align-items: center;
    gap: 8px;
    font-size: 17px;
    font-weight: 500;
    color: var(--text-light);
  }
  .address .icon { width: 14px; height: 18px; }
</style>
</head>
<body>
<main class="canvas">

  <section class="card card--front" aria-label="Business card front">
    <div class="brand">
      <span class="brand__square"></span>
      <span class="brand__name">
        <span class="brand__title">PL Ledgerworth</span>
        <span class="brand__tagline">Chartered Accountants</span>
      </span>
    </div>
    <p class="front-website">www.plledgerworth.com.au</p>
  </section>

  <section class="card card--back" aria-label="Business card back">
    <div class="person">
      <h1 class="person__name">Mara Osei</h1>
      <p class="person__role">Manager</p>
    </div>

    <span class="divider"></span>

    <ul class="contacts">
      <li class="contacts__item">
        <svg class="icon" viewBox="0 0 24 24" aria-hidden="true"><path d="M6.6 10.8c1.4 2.8 3.8 5.1 6.6 6.6l2.2-2.2c.3-.3.7-.4 1-.2 1.1.4 2.3.6 3.6.6.6 0 1 .4 1 1V20c0 .6-.4 1-1 1C10.6 21 3 13.4 3 4c0-.6.4-1 1-1h3.5c.6 0 1 .4 1 1 0 1.3.2 2.5.6 3.6.1.3 0 .7-.2 1z"/></svg>
        02 9314 2758
      </li>
      <li class="contacts__item">
        <svg class="icon" viewBox="0 0 24 24" aria-hidden="true"><path d="M7 1h10c1.1 0 2 .9 2 2v18c0 1.1-.9 2-2 2H7c-1.1 0-2-.9-2-2V3c0-1.1.9-2 2-2zm0 3v14h10V4zm5 15.5a1.2 1.2 0 1 0 0 2.4 1.2 1.2 0 0 0 0-2.4z"/></svg>
        04 5127 8830
      </li>
      <li class="contacts__item">
        <svg class="icon" viewBox="0 0 24 24" aria-hidden="true"><circle cx="12" cy="12" r="10"/></svg>
        9081726
      </li>
      <li class="contacts__item">
        <svg class="icon" viewBox="0 0 24 24" aria-hidden="true"><path d="M2 5h20v14H2zm2 2v.6l8 5.2 8-5.2V7zm0 3v7h16v-7l-8 5.2z"/></svg>
        mara@plledgerworth.com.au
      </li>
      <li class="contacts__item">
        <svg class="icon" viewBox="0 0 24 24" aria-hidden="true"><path d="M12 2a10 10 0 1 0 0 20 10 10 0 0 0 0-20zm6.9 6h-2.9a15.7 15.7 0 0 0-1.4-3.6A8 8 0 0 1 18.9 8zM12 4c.8 1.2 1.5 2.5 1.9 4h-3.8c.4-1.5 1.1-2.8 1.9-4zM4.3 14a8 8 0 0 1 0-4h3.4a16.5 16.5 0 0 0 0 4zm.8 2h2.9c.3 1.3.8 2.5 1.4 3.6A8 8 0 0 1 5.1 16zM8 8H5.1a8 8 0 0 1 4.3-3.6C8.8 5.5 8.4 6.7 8 8zm4 12c-.8-1.2-1.5-2.5-1.9-4h3.8c-.4 1.5-1.1 2.8-1.9 4zm2.3-6H9.7a14.7 14.7 0 0 1 0-4h4.6a14.7 14.7 0 0 1 0 4zm.3 5.6c.6-1.1 1.1-2.3 1.4-3.6h2.9a8 8 0 0 1-4.3 3.6zm1.7-5.6a16.5 16.5 0 0 0 0-4h3.4a8 8 0 0 1 0 4z"/></svg>
        www.plledgerworth.com.au
      </li>
    </ul>

    <p class="address">
      <svg class="icon" viewBox="0 0 24 30" aria-hidden="true"><path d="M12 0C5.4 0 0 5.3 0 11.9 0 20.8 12 30 12 30s12-9.2 12-18.1C24 5.3 18.6 0 12 0zm0 16.5a4.6 4.6 0 1 1 0-9.2 4.6 4.6 0 0 1 0 9.2z"/></svg>
      Level 9, 42 Garnet Lane, Sydney NSW 2000
    </p>
  </section>

</main>
</body>
</html>
```